Business Card Design

We need a business card designed for our new company. Prefer a black card with white logo & writing.

Contact Information for Business Card

Dale Pickett, address: 7-4417 Larchmere Avenue, Abbotsford, BC, V3K 2R9, Office Phone: 604-555-0172, Cell: 604-555-0138, Email: dale@kelsoncoatworks.ca

Colors

Designer to choose only greyscale colors for use in the design.

```html
<!DOCTYPE html>
<html lang="en">
<head>
<meta charset="utf-8">
<title>Kelson Coatworks — Business Card</title>
<link rel="stylesheet" href="https://fonts.googleapis.com/css2?family=Poppins:wght@700&family=Raleway:wght@300;400&display=swap">
<style>
  :root {
    --page: #ffffff;
    --card-black: #1e1a1a;
    --panel-grey: #4b4848;
    --stripe-grey: #7f7d7d;
    --stripe-white: #ffffff;
    --badge-grey: #7a7878;
    --ink: #ffffff;
    --ink-soft: #e4e2e2;
  }
  * { margin: 0; padding: 0; box-sizing: border-box; }
  html, body {
    width: 1200px; height: 999px; overflow: hidden;
    background: var(--page);
  }
  .stage {
    position: relative;
    width: 1280px; height: 1066px;
    transform: scale(0.9375);
    transform-origin: 0 0;
  }
  .card {
    position: absolute;
    left: 222px;
    width: 776px; height: 433px;
    background: var(--card-black);
    box-shadow: 0 22px 30px -14px rgba(0,0,0,0.28);
    overflow: hidden;
  }
  .card--front { top: 55px; }
  .card--back { top: 549px; }
  .card__art { position: absolute; inset: 0; width: 100%; height: 100%; }

  .wordmark {
    position: absolute;
    color: var(--ink);
    font-family: "Poppins", sans-serif;
    font-weight: 700;
    text-align: center;
    text-transform: uppercase;
    line-height: 1.05;
  }
  .wordmark--small {
    left: 30px; top: 92px; width: 250px;
    font-size: 30px; letter-spacing: 1px;
  }
  .wordmark--large {
    left: 0; right: 0; top: 168px;
    font-size: 46px; letter-spacing: 2px;
  }

  .holder-name {
    position: absolute;
    right: 60px; top: 128px;
    color: var(--ink);
    font-family: "Raleway", sans-serif;
    font-weight: 300;
    font-size: 35px;
    letter-spacing: 3px;
    text-transform: uppercase;
  }
  .contact-list {
    position: absolute;
    left: 356px; top: 200px;
    list-style: none;
    font-family: "Raleway", sans-serif;
    font-weight: 400;
    font-size: 19px;
    letter-spacing: 1.4px;
    text-transform: uppercase;
    color: var(--ink-soft);
  }
  .contact-item {
    position: relative;
    display: flex;
    align-items: flex-start;
    margin-bottom: 15px;
  }
  .contact-item__badge {
    width: 34px; height: 34px;
    border-radius: 50%;
    background: var(--badge-grey);
    color: var(--ink);
    font-size: 21px;
    display: flex; align-items: center; justify-content: center;
    flex: none;
  }
  .contact-item__text {
    margin-left: 26px;
    line-height: 27px;
    padding-top: 4px;
  }
</style>
</head>
<body>
<main class="stage">

  <section class="card card--front" aria-label="Card front">
    <svg class="card__art" viewBox="0 0 776 433" aria-hidden="true">
      <rect width="776" height="433" fill="var(--card-black)"/>
      <polygon points="503,0 776,0 776,433 73,433" fill="var(--panel-grey)"/>
      <polygon points="398,75 428,75 72,433 42,433" fill="var(--stripe-grey)"/>
      <polygon points="363,90 383,90 42,433 22,433" fill="var(--stripe-white)"/>
    </svg>

    <div class="wordmark wordmark--small">Kelson<br>Coatworks</div>

    <h1 class="holder-name">Dale Pickett</h1>

    <ul class="contact-list">
      <li class="contact-item">
        <span class="contact-item__badge">A</span>
        <span class="contact-item__text">7-4417 Larchmere Avenue,<br>Abbotsford, BC, V3K 2R9</span>
      </li>
      <li class="contact-item">
        <span class="contact-item__badge">P</span>
        <span class="contact-item__text">604-555-0172</span>
      </li>
      <li class="contact-item">
        <span class="contact-item__badge">C</span>
        <span class="contact-item__text">604-555-0138</span>
      </li>
      <li class="contact-item">
        <span class="contact-item__badge">E</span>
        <span class="contact-item__text">dale@kelsoncoatworks.ca</span>
      </li>
    </ul>
  </section>

  <section class="card card--back" aria-label="Card back">
    <div class="wordmark wordmark--large">Kelson<br>Coatworks</div>
  </section>

</main>
</body>
</html>
```